Zielgruppe
vertica plus ist eine Vertriebsagentur, die sich ausschließlich auf den BtoB Vertrieb spezialisiert hat. Wir agieren seit 19 Jahren am Markt und sind mehrfach ausgezeichneter Exzellenzberater des Mittelstandes. Wir unterstützen mittelständische Unternehmen, Familienunternehmen, Start up´s in der Wachstumsphase und Großkonzerne in der Industrie und im Dienstleistungsbereich. Ansprechpartner für uns sind Vertriebsleiter und GF´s in den Unternehmen.
Aufgabenstellung
Wir möchten unsere Angebotsvorlage neu im Layout neu designen lassen. Sie soll unsere Arbeitsweise zielgenau - authentisch - pfiffig widerspiegeln. Ich möchte gerne eine moderne und klare Struktur. Auf einer Seite sollen unsere USP´s dargestellt werden und auf ein - zwei Seiten ist das Angebot - in den folgenden Seiten sind die Vertragsinhalte.

```html
<!DOCTYPE html>
<html lang="de">
<head>
<meta charset="utf-8">
<title>vertica plus – Angebotsvorlage</title>
<link href="https://fonts.googleapis.com/css2?family=Arimo:wght@400;700&display=swap" rel="stylesheet">
<style>
  :root {
    --backdrop: #e4e2de;
    --paper: #ffffff;
    --panel: #403c41;
    --brand-blue: #1f4b9c;
    --accent-red: #e0452b;
    --ink: #222222;
    --rule: #c9c9c9;
    --white: #ffffff;
  }
  html, body {
    margin: 0;
    padding: 0;
    width: 1200px;
    height: 1200px;
    overflow: hidden;
    background: var(--backdrop);
    font-family: "Arimo", Arial, sans-serif;
  }
  .spread { position: relative; width: 1200px; height: 1200px; }
  .page {
    position: absolute;
    top: 218px;
    width: 540px;
    height: 764px;
    background: var(--paper);
    box-shadow: 0 4px 14px rgba(0,0,0,0.18);
    overflow: hidden;
  }
  .page--cover { left: 45px; }
  .page--intro { left: 615px; }
  .page svg.art { position: absolute; inset: 0; }

  /* cover */
  .cover-title {
    position: absolute;
    left: 292px;
    top: 300px;
    margin: 0;
    color: var(--white);
    font-weight: 400;
    font-size: 25px;
    line-height: 1.18;
  }
  .cover-info {
    position: absolute;
    left: 292px;
    width: 150px;
    color: var(--white);
    font-size: 9.5px;
    line-height: 1.45;
  }
  .cover-info h3 {
    margin: 0 0 4px;
    font-size: 9.5px;
    font-weight: 700;
    padding-bottom: 4px;
    border-bottom: 1px solid rgba(255,255,255,0.55);
  }
  .cover-info p { margin: 0; }
  .cover-info--contact { top: 440px; }
  .cover-info--location { top: 510px; }
  .brand-name {
    position: absolute;
    left: 410px;
    top: 668px;
    margin: 0;
    color: var(--brand-blue);
    font-size: 21px;
    font-weight: 700;
    letter-spacing: -0.3px;
    white-space: nowrap;
  }

  /* intro */
  .page-number {
    position: absolute;
    left: 26px;
    top: 26px;
    color: var(--white);
    font-size: 7px;
  }
  .offer-number {
    position: absolute;
    right: 26px;
    top: 94px;
    margin: 0;
    color: var(--accent-red);
    font-size: 10px;
  }
  .intro-headline {
    position: absolute;
    left: 118px;
    top: 366px;
    margin: 0;
    color: var(--brand-blue);
    font-weight: 400;
    font-size: 58px;
    line-height: 0.98;
    letter-spacing: 1px;
  }
  .intro-copy {
    position: absolute;
    left: 262px;
    top: 556px;
    width: 250px;
    color: var(--ink);
    font-size: 9px;
    line-height: 1.38;
  }
  .intro-copy p { margin: 0 0 10px; }
  .contact-footer {
    position: absolute;
    left: 26px;
    right: 26px;
    top: 714px;
    padding-bottom: 6px;
    border-bottom: 1px solid var(--rule);
    color: var(--ink);
    font-size: 9.5px;
    white-space: nowrap;
  }
</style>
</head>
<body>
<main class="spread">

  <section class="page page--cover">
    <svg class="art" width="540" height="764" viewBox="0 0 540 764">
      <defs>
        <linearGradient id="coverPhotoTone" x1="0" y1="0" x2="0.4" y2="1">
          <stop offset="0" stop-color="#cfc6ba"/>
          <stop offset="0.45" stop-color="#e9e3dc"/>
          <stop offset="1" stop-color="#6f645b"/>
        </linearGradient>
        <clipPath id="coverArch">
          <path d="M30 95 H510 V480 A240 240 0 0 1 30 480 Z"/>
        </clipPath>
      </defs>
      <g clip-path="url(#coverArch)">
        <rect x="0" y="0" width="540" height="764" fill="url(#coverPhotoTone)"
              role="img" aria-label="Foto: Beraterin in weißer Bluse, lächelnd an einer Glaswand im Büro"/>
        <rect x="230" y="640" width="170" height="90" fill="var(--brand-blue)"/>
      </g>
      <rect x="270" y="40" width="195" height="600" fill="var(--panel)"/>
    </svg>

    <h1 class="cover-title">Unsere<br>Erahrung,<br>Ihr Vorsprung.</h1>

    <div class="cover-info cover-info--contact">
      <h3>Kontakt</h3>
      <p>Katrin Albers-Wendt<br>+49 (0) 170 284 613 7<br>kaw@vertica-plus.de</p>
    </div>
    <div class="cover-info cover-info--location">
      <h3>Standort</h3>
      <p>Lindenweg 12<br>91054 Erlangen</p>
    </div>

    <p class="brand-name">vertica plus</p>
  </section>

  <section class="page page--intro">
    <svg class="art" width="540" height="764" viewBox="0 0 540 764">
      <defs>
        <linearGradient id="portraitTone" x1="0" y1="0" x2="0.3" y2="1">
          <stop offset="0" stop-color="#3a2e28"/>
          <stop offset="0.4" stop-color="#8a6a52"/>
          <stop offset="0.75" stop-color="#c9553a"/>
          <stop offset="1" stop-color="#d8452a"/>
        </linearGradient>
        <clipPath id="portraitTop">
          <rect x="0" y="30" width="540" height="734"/>
        </clipPath>
      </defs>
      <circle cx="200" cy="280" r="260" fill="url(#portraitTone)" clip-path="url(#portraitTop)"
              role="img" aria-label="Porträtfoto: Beraterin mit blonden Locken in roter Jacke"/>
      <line x1="26" y1="44" x2="300" y2="44" stroke="var(--white)" stroke-width="1.5"/>
      <line x1="400" y1="112" x2="514" y2="112" stroke="var(--rule)" stroke-width="1.5"/>
    </svg>

    <span class="page-number">2</span>
    <p class="offer-number">Angebot-Nr. 20221008</p>

    <h2 class="intro-headline">NEUE<br>MÄRKTE<br>EROBERN</h2>

    <div class="intro-copy">
      <p>Wir sind der Turbo für Ihren Vertrieb und gehören zu den 10 führenden Anbietern im B2B-Vertrieb. Wir bewegen uns sicher in der Akquise in der oberen Führungsebene bis zum DAX-Konzern. Wir bieten eine 720°strukturierte Vertriebsberatung, -umsetzung und –kontrolle: von A (Analyse) – Z (Verkauf). Wir denken vor und zurück, reflektieren Gespräche und Zielgruppe.</p>
      <p>Wir sind zum 3. Mal in Folge als Exzellenzberater Deutscher Mittelstand im Vertrieb ausgezeichnet!</p>
    </div>

    <div class="contact-footer">+49 (0) 170 284 613 7 &nbsp;|&nbsp; kaw@vertica-plus.de &nbsp;|&nbsp; Lindenweg 12 &nbsp;|&nbsp; 91054 Erlangen &nbsp;|&nbsp; 09131 462 380 0</div>
  </section>

</main>
</body>
</html>
```